Postcard Design

I have a vacation rental business in Burnet, Texas in the Texas Hill Country. I need a one page flyer type handout for use with the local area chambers of commerce.

I have a website - www.quillmeadowlodges.com

I have a business card - that Pressolux did the printing on

Requirements
Must have
• Need to have an arrowhead in the design

Need you to go to the website for some of the information and then the flyer needs to have all the business card information on it too.
Nice to have
• Printing on both sides

```html
<!DOCTYPE html>
<html lang="en">
<head>
<meta charset="utf-8">
<title>Quill Meadow Lodges Postcard</title>
<link href="https://fonts.googleapis.com/css2?family=Cormorant+SC:wght@500;700&family=Crimson+Text:ital,wght@0,400;0,600;0,700;1,600;1,700&display=swap" rel="stylesheet">
<style>
  :root {
    --page: #e4e4e1;
    --olive: #3c4427;
    --olive-text: #3e4a22;
    --cream: #f1efe6;
    --plate: #e9eae5;
    --white: #ffffff;
    --ink: #111111;
    --night: #0d0d0d;
    --bar-top: #fbfbfb;
    --bar-bottom: #cfd2d4;
    --tab: #4d6a2f;
    --tab-light: #7c9a57;
  }
  * { box-sizing: border-box; margin: 0; padding: 0; }
  html, body { width: 1200px; height: 1000px; overflow: hidden; }
  body { background: var(--page); position: relative; font-family: "Crimson Text", serif; }

  .sheet-title {
    position: absolute; left: 27px; top: 28px;
    font-family: "Cormorant SC", serif; font-weight: 700;
    font-size: 36px; color: var(--olive-text); letter-spacing: 0.3px;
  }
  .sheet-title .tag { font-weight: 500; }
  .sheet-side {
    position: absolute; right: 28px; top: 38px;
    font-family: "Crimson Text", serif; font-size: 28px;
    color: var(--olive-text); letter-spacing: 1px;
  }

  .card {
    position: absolute; left: 26px; top: 75px; width: 1147px; height: 884px;
    border: 1px solid #b9bab5; background: var(--olive);
    box-shadow: 0 1px 3px rgba(0,0,0,.15);
  }

  .story {
    position: absolute; left: 0; top: 0; width: 554px; height: 882px;
    background: var(--olive); color: var(--cream);
  }
  .brand-plate {
    position: absolute; left: 169px; top: 19px; width: 223px; height: 146px;
    background: var(--plate); border: 3px solid var(--plate);
    outline: 2px solid var(--olive); outline-offset: -9px;
    display: flex; flex-direction: column; align-items: center; justify-content: center;
    text-align: center; gap: 12px;
  }
  .brand-name {
    font-family: "Crimson Text", serif; font-weight: 600; font-size: 24px; line-height: 26px;
    color: var(--olive); letter-spacing: 1.5px;
  }
  .brand-mark { width: 16px; height: 16px; background: var(--olive); }
  .kicker {
    position: absolute; left: 0; width: 554px; top: 180px; text-align: center;
    font-family: "Crimson Text", serif; font-style: italic; font-weight: 700;
    font-size: 21px; color: var(--cream); letter-spacing: .3px;
  }
  .kicker::before, .kicker::after {
    content: ""; display: inline-block; width: 40px; height: 1px;
    background: var(--cream); vertical-align: middle; margin: 0 12px;
  }
  .about {
    position: absolute; left: 34px; top: 232px; width: 496px;
    font-size: 20.6px; line-height: 35px; text-align: justify; color: var(--cream);
  }

  .scene {
    position: absolute; left: 555px; top: 0; width: 590px; height: 700px;
    background: linear-gradient(180deg, #a9898f 0%, #cf9e98 35%, #e6a58e 62%, #c89a98 70%, #5a5257 74%, #3a3a40 100%);
  }

  .contact {
    position: absolute; left: 555px; top: 520px; width: 590px;
    font-family: "Crimson Text", serif; color: var(--white);
  }
  .contact-lead {
    position: absolute; left: 20px; top: 0; font-weight: 700; font-size: 19.5px;
  }
  .contact-row { position: absolute; left: 0; height: 40px; display: flex; align-items: center; }
  .contact-row .tab { width: 60px; height: 40px; }
  .contact-row .value { margin-left: 8px; font-size: 27px; }
  .contact-row.phone { top: 38px; }
  .contact-row.phone .value { font-size: 34px; font-weight: 700; }
  .contact-row.mail { top: 80px; }
  .contact-row.web { top: 121px; }
  .contact-row.web b { font-weight: 700; }

  .listing-bar {
    position: absolute; left: 555px; top: 700px; width: 590px; height: 38px;
    background: linear-gradient(180deg, var(--bar-top), var(--bar-bottom));
    font-family: "Crimson Text", serif; font-size: 21px; color: var(--ink);
    padding-left: 20px; display: flex; align-items: center;
  }
  .listing-bar b { font-weight: 700; margin: 0 6px; }
  .listing-bar .chev { margin-left: 10px; font-size: 24px; }

  .memberships {
    position: absolute; left: 555px; top: 738px; width: 590px; height: 144px;
    background: var(--night); color: var(--white);
    font-family: "Crimson Text", serif; padding: 14px 0 0 21px;
  }
  .memberships h3 { font-size: 20px; font-weight: 700; margin-bottom: 2px; }
  .memberships ul { list-style: none; }
  .memberships li { font-size: 21px; line-height: 28px; }
  .memberships li em { font-weight: 600; font-style: italic; }
  .memberships li::before { content: "›"; margin-right: 9px; font-size: 22px; }
</style>
</head>
<body>
  <div class="sheet-title">Quill Meadow Lodges <span class="tag">Postcard</span></div>
  <div class="sheet-side">BACK</div>

  <main class="card">
    <section class="story">
      <div class="brand-plate">
        <span class="brand-name">QUILL MEADOW<br>LODGES</span>
        <span class="brand-mark"></span>
      </div>
      <p class="kicker">Private Property Cabins</p>
      <p class="about">Quill Meadow Lodges on Lake Buchanan offers privacy and seclusion on 20 acres of lakefront property on the uppermost of the Highland Lakes in the beautiful Texas Hill Country. The property is located on RR 4410 on the deep side of Lake Buchanan, surrounded by spectacular fields of bluebonnets and other wild flowers in the spring. The property boasts a main “log cabin” lodge and three additional cabins that are also available for rental based on your group size. The cabins can accommodate 6 to 28 overnight guests and larger groups for the day for weddings, family reunions and corporate retreats. Quill Meadow Lodges is located directly across from “White Bluff,” a large limestone formation carved by an underground spring. The property is named for the numerous, ancient arrowheads in the lakebed where the creek from White Bluff empties into Lake Buchanan. Bring your trowel to see what you can find!</p>
    </section>

    <div class="scene" role="img" aria-label="Photo of a sunset over Lake Buchanan with a tree silhouette and a dock"></div>

    <section class="contact">
      <p class="contact-lead">Please contact us for bookings and more information:</p>
      <div class="contact-row phone">
        <svg class="tab" viewBox="0 0 60 40"><polygon points="0,0 60,0 48,20 60,40 0,40" fill="var(--tab)"/><polygon points="0,0 60,0 48,20 0,20" fill="var(--tab-light)" opacity=".5"/><path d="M20 12c2 -1 3 0 3 2l-1 3c0 1 2 5 4 6l2 -1c2 0 3 1 2 3l-1 2c-6 1 -12 -7 -9 -15z" fill="var(--white)"/></svg>
        <span class="value">(512) 555-0148</span>
      </div>
      <div class="contact-row mail">
        <svg class="tab" viewBox="0 0 60 40"><polygon points="0,0 60,0 48,20 60,40 0,40" fill="var(--tab)"/><polygon points="0,0 60,0 48,20 0,20" fill="var(--tab-light)" opacity=".5"/><rect x="13" y="12" width="24" height="16" fill="var(--white)"/><path d="M13 12 L25 22 L37 12" stroke="var(--tab)" stroke-width="2" fill="none"/></svg>
        <span class="value">info@quillmeadowlodges.com</span>
      </div>
      <div class="contact-row web">
        <svg class="tab" viewBox="0 0 60 40"><polygon points="0,0 60,0 48,20 60,40 0,40" fill="var(--tab)"/><polygon points="0,0 60,0 48,20 0,20" fill="var(--tab-light)" opacity=".5"/><g fill="none" stroke="var(--white)" stroke-width="3"><rect x="14" y="18" width="12" height="7" rx="3.5" transform="rotate(-45 20 21.5)"/><rect x="22" y="12" width="12" height="7" rx="3.5" transform="rotate(-45 28 15.5)"/></g></svg>
        <span class="value">www.<b>quillmeadowlodges</b>.com</span>
      </div>
    </section>

    <div class="listing-bar">See our listing on <b>Staylisting.com</b> and <b>CabinFinder.com</b> <span class="chev">›</span></div>

    <section class="memberships">
      <h3>Quill Meadow Lodges is member of:</h3>
      <ul>
        <li>Buchanan Shores/<em>Granite Cove Business Council</em></li>
        <li>Kingsland/<em>Cedar Point Business Council</em></li>
        <li>Marble Falls/<em>Cedar Point Business Council</em></li>
      </ul>
    </section>
  </main>
</body>
</html>
```